Lumo -Fresh business card design

It is a dry cleaning carpet business.
Red wine stain removal and pet urine treatments.
Servicing all regional areas.

all logo and pictures files have been uploaded

Industry/Entity Type

Dry Cleaning

Contact Information for Business Card

Lumo-Fresh Carpet and upholstery cleaning.
Servicing Albury/Wodonga and surrounding areas.
ph greg 0413572960 ,email lumofresh1@kestrelmail.com

Font styles to use
Serif
Sans Serif
Other font styles liked:
• lumo fresh logo font

Colors
ec2027
ffcf3e
33a6d7
0692cd

Requirements
Nice to have
• I have included photos of the logo and car and stripe on van ,I dont need all of them in the card just i would like to stick to these colours.

```html
<!DOCTYPE html>
<html lang="en">
<head>
<meta charset="utf-8">
<title>Lumo-Fresh Business Card</title>
<link rel="stylesheet" href="https://fonts.googleapis.com/css2?family=Exo+2:wght@400;500;600;800&display=swap">
<style>
  :root {
    --backdrop: #e4e4e6;
    --card: #ffffff;
    --blue-deep: #1f4fb3;
    --blue-bright: #0aa9e8;
    --brand-blue: #0692cd;
    --tagline-blue: #5a82d2;
    --swoosh-dark: #6f7278;
    --swoosh-light: #d9dadd;
    --ink: #2a2a2e;
    --icon-red: #ec2027;
    --white: #ffffff;
  }
  * { margin: 0; padding: 0; box-sizing: border-box; }
  html, body {
    width: 1200px; height: 900px; overflow: hidden;
    background: var(--backdrop);
    font-family: "Exo 2", sans-serif;
  }
  .business-card {
    position: absolute; left: 100px; top: 164px;
    width: 1000px; height: 572px;
    background: var(--card);
    box-shadow: 0 14px 34px rgba(0,0,0,.18);
    overflow: hidden;
  }
  .card-header-band { position: absolute; inset: 0; width: 1000px; height: 572px; }
  .holder { position: absolute; right: 60px; top: 22px; text-align: right; color: var(--white); }
  .holder-name { font-size: 30px; font-weight: 500; letter-spacing: 1.5px; text-transform: uppercase; }
  .holder-title { font-size: 21px; font-weight: 400; margin-top: 2px; }
  .brand { position: absolute; left: 70px; top: 318px; }
  .brand-name {
    font-size: 76px; font-weight: 800; color: var(--brand-blue);
    line-height: 1; letter-spacing: 1px; white-space: nowrap;
  }
  .brand-tagline {
    margin-top: 6px; font-size: 28px; font-weight: 600; color: var(--tagline-blue);
    line-height: 1.05; text-align: center; letter-spacing: 1px;
  }
  .address {
    position: absolute; left: 70px; bottom: 34px;
    font-size: 22px; font-style: normal; color: var(--ink);
    line-height: 1.25; letter-spacing: .5px;
  }
  .contact-list { position: absolute; right: 48px; top: 122px; list-style: none; }
  .contact-item {
    display: flex; justify-content: flex-end; align-items: center; gap: 14px;
    height: 38px; font-size: 21px; color: var(--ink); letter-spacing: .6px;
  }
  .contact-icon { width: 21px; height: 21px; flex: none; }
</style>
</head>
<body>
  <main class="business-card">
    <svg class="card-header-band" viewBox="0 0 1000 572" aria-hidden="true">
      <defs>
        <radialGradient id="bandBlue" cx="45%" cy="60%" r="70%">
          <stop offset="0" stop-color="var(--blue-bright)"/>
          <stop offset="1" stop-color="var(--blue-deep)"/>
        </radialGradient>
        <linearGradient id="swooshGrey" x1="0" y1="0" x2="1" y2="0">
          <stop offset="0" stop-color="var(--swoosh-dark)"/>
          <stop offset=".55" stop-color="var(--swoosh-light)"/>
          <stop offset="1" stop-color="var(--card)"/>
        </linearGradient>
      </defs>
      <path d="M0 0H1000V100C700 110 430 158 260 212C170 240 80 248 0 250Z" fill="url(#swooshGrey)"/>
      <path d="M0 0H1000V82C700 90 430 138 260 190C170 218 80 226 0 228Z" fill="url(#bandBlue)"/>
    </svg>

    <header class="holder">
      <p class="holder-name">Greg Hollis</p>
      <p class="holder-title">Managing Director</p>
    </header>

    <section class="brand">
      <h1 class="brand-name">LUMO-FRESH</h1>
      <p class="brand-tagline">CARPET &amp; UPHOLSTERY<br>CLEANING</p>
    </section>

    <address class="address">
      Unit 3, 18 Kestrel Way<br>Albury NSW
    </address>

    <ul class="contact-list">
      <li class="contact-item">02 6041 5820
        <svg class="contact-icon" viewBox="0 0 24 24" aria-hidden="true"><path fill="var(--icon-red)" d="M6.6 2.5l3 3.4-1.8 2.4a12 12 0 0 0 7.9 7.9l2.4-1.8 3.4 3-1.7 3.1C11 20 4 13 3.5 4.2z"/></svg>
      </li>
      <li class="contact-item">0413 572 960
        <svg class="contact-icon" viewBox="0 0 24 24" aria-hidden="true"><rect x="6" y="2" width="12" height="20" rx="2" fill="none" stroke="var(--icon-red)" stroke-width="2.2"/><circle cx="12" cy="18" r="1.3" fill="var(--icon-red)"/></svg>
      </li>
      <li class="contact-item">02 6041 5821
        <svg class="contact-icon" viewBox="0 0 24 24" aria-hidden="true"><rect x="7" y="2" width="10" height="7" fill="var(--icon-red)"/><rect x="3" y="10" width="18" height="11" rx="1.5" fill="var(--icon-red)"/><rect x="7" y="13" width="10" height="2" fill="var(--white)"/></svg>
      </li>
      <li class="contact-item">lumofresh1@kestrelmail.com
        <svg class="contact-icon" viewBox="0 0 24 24" aria-hidden="true"><rect x="2" y="5" width="20" height="14" rx="1.5" fill="var(--icon-red)"/><path d="M3 6l9 7 9-7" fill="none" stroke="var(--white)" stroke-width="1.8"/></svg>
      </li>
      <li class="contact-item">www.lumofreshcleaning.com
        <svg class="contact-icon" viewBox="0 0 24 24" aria-hidden="true"><circle cx="12" cy="12" r="10" fill="var(--icon-red)"/><g fill="none" stroke="var(--white)" stroke-width="1.4"><ellipse cx="12" cy="12" rx="4.5" ry="10"/><path d="M2 12h20M4 7h16M4 17h16"/></g></svg>
      </li>
    </ul>
  </main>
</body>
</html>
```